Global E-commerce Business Needs Banner Ad

We need banner ads for a fast growing E-commerce business cater mostly to women. The ads must have unique and beautiful background that accentuate the products. The ads should also have between 1-4 products in it. It needs to have the headline "Up To 80% Off Retail" in the ad. The ad also needs to have our logo and a "View Now" button. The ad should be more feminine and playful. Each product should have a different background design specially for the product to make it more beautiful.

Dimension: 320 by 480 pixel

Target Market(s)

Women

Industry/Entity Type

Business

Requirements
Must have
• 1) "Up To 80% Off Retail"
• 2) Brimvale Logo
• 3) "View Now" button

```html
<!DOCTYPE html>
<html lang="en">
<head>
<meta charset="utf-8">
<title>Brimvale Banner Ad</title>
<link rel="stylesheet" href="https://fonts.googleapis.com/css2?family=Open+Sans:wght@300;400&family=Oswald:wght@400;600;700&display=swap">
<style>
  :root {
    --backdrop: #6f6f6f;
    --purple-deep: #4a2a86;
    --purple-mid: #6a45ad;
    --purple-light: #8a67c6;
    --pink: #ec1e7a;
    --pink-bright: #ff3d96;
    --yellow: #fff200;
    --white: #ffffff;
    --ink: #2a2a2a;
    --peach: #ffc98f;
    --sky: #7fd2f2;
    --rose: #ffa9b9;
  }
  * { box-sizing: border-box; margin: 0; padding: 0; }
  html, body { width: 1200px; height: 1200px; overflow: hidden; }
  body {
    background: var(--backdrop);
    font-family: "Open Sans", Arial, sans-serif;
    position: relative;
  }
  .banner {
    position: absolute;
    left: 248px;
    top: 72px;
    width: 320px;
    height: 480px;
    transform: scale(2.2);
    transform-origin: 0 0;
    overflow: hidden;
    background: radial-gradient(ellipse at 50% 45%, var(--purple-light) 0%, var(--purple-mid) 45%, var(--purple-deep) 100%);
  }
  .brand {
    position: absolute;
    left: 40px;
    top: 24px;
    color: var(--white);
    font-weight: 300;
    font-size: 18px;
    letter-spacing: 0.3px;
    line-height: 1;
  }
  .headline-badge {
    position: absolute;
    z-index: 3;
    left: 169px;
    top: -23px;
    width: 136px;
    height: 136px;
    border-radius: 50%;
    border: 4px solid var(--white);
    background: radial-gradient(circle at 45% 40%, var(--pink-bright), var(--pink) 70%);
    box-shadow: 0 3px 8px rgba(0,0,0,0.35);
    display: flex;
    flex-direction: column;
    align-items: center;
    justify-content: center;
    padding-top: 18px;
    color: var(--white);
    font-family: "Oswald", "Arial Narrow", sans-serif;
    text-align: center;
    line-height: 1;
  }
  .headline-badge .lead { font-size: 19px; font-weight: 400; }
  .headline-badge .amount { font-size: 28px; font-weight: 700; color: var(--yellow); margin: 3px 0 2px; }
  .headline-badge .tail { font-size: 19px; font-weight: 400; }
  .product {
    position: absolute;
    z-index: 1;
    left: 33px;
    width: 252px;
    height: 114px;
    box-shadow: 0 2px 6px rgba(0,0,0,0.3);
  }
  .product--gold { top: 68px; background: linear-gradient(90deg, var(--white) 30%, var(--peach) 100%); }
  .product--sapphire { top: 192px; height: 113px; background: linear-gradient(90deg, var(--sky) 0%, var(--white) 75%); }
  .product--onyx { top: 317px; height: 112px; background: linear-gradient(90deg, var(--white) 35%, var(--rose) 100%); }
  .product-photo { position: absolute; border-radius: 40%; }
  .product--gold .product-photo { left: 20px; top: 8px; width: 72px; height: 96px; background: radial-gradient(ellipse, #e8e8ee 0%, #d9a760 55%, rgba(217,167,96,0) 75%); }
  .product--sapphire .product-photo { left: 150px; top: 10px; width: 70px; height: 94px; background: radial-gradient(ellipse, #e0218a 0%, #b9c2cf 55%, rgba(185,194,207,0) 75%); }
  .product--onyx .product-photo { left: 18px; top: 8px; width: 92px; height: 94px; background: radial-gradient(ellipse, #f27ab0 0%, #2c2c32 50%, rgba(44,44,50,0) 75%); }
  .product-name {
    position: absolute;
    font-weight: 300;
    font-size: 16px;
    color: var(--ink);
    line-height: 1;
    white-space: nowrap;
  }
  .product--gold .product-name { right: 12px; top: 74px; }
  .product--sapphire .product-name { left: 10px; top: 73px; }
  .product--onyx .product-name { right: 12px; top: 72px; }
  .discount-tag {
    position: absolute;
    top: 0;
    width: 32px;
    height: 56px;
    background: var(--pink);
    border-radius: 0 0 6px 6px;
    color: var(--yellow);
    font-family: "Oswald", "Arial Narrow", sans-serif;
    font-weight: 400;
    text-align: center;
    line-height: 1;
    padding-top: 8px;
  }
  .discount-tag .pct { font-size: 15px; }
  .discount-tag .pct sup { font-size: 8px; }
  .discount-tag .off { font-size: 15px; display: block; margin-top: 2px; }
  .product--sapphire .discount-tag { left: 10px; }
  .product--onyx .discount-tag { right: 13px; }
  .cta-rule {
    position: absolute;
    top: 455px;
    width: 44px;
    height: 1px;
    background: var(--white);
  }
  .cta-rule--left { left: 33px; }
  .cta-rule--right { left: 241px; }
  .view-now {
    position: absolute;
    left: 102px;
    top: 440px;
    width: 117px;
    height: 30px;
    border: 1px solid var(--white);
    color: var(--yellow);
    font-size: 15px;
    display: flex;
    align-items: center;
    justify-content: center;
    gap: 6px;
    text-decoration: none;
  }
</style>
</head>
<body>
  <div class="banner">
    <div class="brand">BRIMVALE</div>

    <div class="headline-badge">
      <span class="lead">Up To</span>
      <span class="amount">80% OFF</span>
      <span class="tail">Retail</span>
    </div>

    <div class="product product--gold">
      <div class="product-photo" role="img" aria-label="Gold ring with pavé diamonds and a solitaire stone"></div>
      <span class="product-name">Name Here</span>
    </div>

    <div class="product product--sapphire">
      <div class="discount-tag"><span class="pct">80<sup>%</sup></span><span class="off">OFF</span></div>
      <div class="product-photo" role="img" aria-label="Silver ring with pink and blue gemstones"></div>
      <span class="product-name">Name Here</span>
    </div>

    <div class="product product--onyx">
      <div class="discount-tag"><span class="pct">80<sup>%</sup></span><span class="off">OFF</span></div>
      <div class="product-photo" role="img" aria-label="Black ring set with a pink centre stone and matching band"></div>
      <span class="product-name">Name Here</span>
    </div>

    <span class="cta-rule cta-rule--left"></span>
    <a class="view-now" href="#">View Now
      <svg width="16" height="10" viewBox="0 0 16 10" aria-hidden="true">
        <path d="M1 5 Q8 -2 15 5 Q8 12 1 5 Z" fill="none" stroke="#fff200" stroke-width="1.3"/>
        <circle cx="8" cy="5" r="2.2" fill="#fff200"/>
      </svg>
    </a>
    <span class="cta-rule cta-rule--right"></span>
  </div>
</body>
</html>
```